Travel Blogger Business Card for roamquill.net

I need a two-sided business card for a travel blogging website. The card should be both professional and fun at the same time. This is for the website www.roamquill.net

I don't necessarily think that the current logo on the website needs to be used on the business card but it can be. I am very flexible with ideas

Target Market(s)

Travel agencies that will be met at a conference.

Industry/Entity Type

Travel

Contact Information for Business Card

Company Name: Roam Quill.net
Name: Bertrand Olesky
Voice: +1-(345)-402-7731
Address: Coral Reach Shore, Grand Cayman, Cayman Islands
Email: ceo@roamquill.net

Colors
0592cd
0355a3
3176b5
33a6d7
85cae6
85acd3

Requirements
Must have
• Website address and name should be bigger than address, phone number, and email.

```html
<!DOCTYPE html>
<html lang="en">
<head>
<meta charset="utf-8">
<title>Roam Quill – Business Card Concepts</title>
<link rel="stylesheet" href="https://fonts.googleapis.com/css2?family=Archivo:wght@400;700&display=swap">
<style>
  :root {
    --stage: #2b2a28;
    --brand-blue: #26509a;
    --sky: #93cbe8;
    --paper: #ffffff;
    --accent-yellow: #ffe800;
    --logo-ink: #e3f5ff;
  }
  html, body {
    margin: 0;
    padding: 0;
    width: 1200px;
    height: 1128px;
    overflow: hidden;
    background: var(--stage);
  }
  .sheet { display: block; width: 1200px; height: 1128px; }
  .card-bg-blue { fill: var(--brand-blue); }
  .card-bg-white { fill: var(--paper); }
  .bubble-white { fill: var(--paper); }
  .bubble-blue { fill: var(--brand-blue); }
  .tag-sky { fill: var(--sky); }
  .art-slot { fill: url(#artGradient); }
  .stripe { stroke: var(--accent-yellow); stroke-width: 5; fill: none; }
  .dash-light { stroke: var(--paper); stroke-width: 1.6; stroke-dasharray: 7 5; fill: none; }
  .dash-blue { stroke: var(--brand-blue); stroke-width: 1.6; stroke-dasharray: 7 5; fill: none; }
  text { font-family: "Archivo", Arial, sans-serif; }
  .holder-name { fill: var(--brand-blue); font-weight: 700; }
  .contact { fill: #222; font-weight: 400; }
  .contact-on-sky { fill: var(--paper); font-weight: 700; }
  .address { fill: #222; font-weight: 400; }
  .brand-name { fill: var(--logo-ink); font-weight: 700; }
  .brand-url { fill: var(--paper); font-weight: 700; }
  .brand-dot { fill: var(--logo-ink); }
</style>
</head>
<body>
<svg class="sheet" viewBox="0 0 1291 1214" xmlns="http://www.w3.org/2000/svg">
  <defs>
    <linearGradient id="artGradient" x1="0" y1="0" x2="0" y2="1">
      <stop offset="0" stop-color="#ffffff"/>
      <stop offset="1" stop-color="#dfe6ee"/>
    </linearGradient>
    <linearGradient id="tailShade" x1="0" y1="0" x2="0" y2="1">
      <stop offset="0" stop-color="#cfcfcf"/>
      <stop offset="1" stop-color="#ffffff"/>
    </linearGradient>
    <clipPath id="c1"><rect x="93" y="75" width="523" height="298"/></clipPath>
    <clipPath id="c2"><rect x="671" y="75" width="523" height="298"/></clipPath>
    <clipPath id="c3"><rect x="91" y="461" width="523" height="297"/></clipPath>
    <clipPath id="c4"><rect x="677" y="461" width="523" height="297"/></clipPath>
    <clipPath id="c5"><rect x="91" y="841" width="523" height="297"/></clipPath>
    <clipPath id="c6"><rect x="677" y="841" width="523" height="297"/></clipPath>
  </defs>

  <rect width="1291" height="1214" fill="var(--stage)"/>

  <!-- Row 1 front -->
  <g class="card card-front" clip-path="url(#c1)">
    <rect class="card-bg-blue" x="93" y="75" width="523" height="298"/>
    <polyline class="dash-light" points="300,75 183,92 165,310 315,328 295,373"/>
    <polyline class="stripe" points="180,140 172,235"/>
    <polyline class="stripe" points="565,75 612,240"/>
    <polyline class="stripe" points="605,285 568,285 585,350 490,340"/>
    <polyline class="stripe" points="440,350 405,373"/>
    <polyline class="dash-light" points="560,75 616,240"/>
    <polygon class="bubble-white" points="250,108 500,75 550,288 240,240"/>
    <polygon fill="url(#tailShade)" points="390,270 470,280 350,360"/>
    <polygon class="tag-sky" points="400,128 548,92 593,232 405,232"/>
    <rect class="art-slot" x="120" y="232" width="140" height="114" role="img" aria-label="Illustration of a white camel"/>
    <text class="holder-name" x="260" y="160" font-size="24">BERTRAND</text>
    <text class="holder-name" x="260" y="194" font-size="24">OLESKY</text>
    <text class="contact-on-sky" x="414" y="167" font-size="16">+1-(345)-402-7731</text>
    <text class="contact-on-sky" x="413" y="189" font-size="14">ceo@roamquill.net</text>
    <text class="address" x="270" y="252" font-size="10.5" transform="rotate(4 270 252)">Coral Reach Shore, Grand Cayman, Cayman Islands</text>
  </g>

  <!-- Row 1 back -->
  <g class="card card-back" clip-path="url(#c2)">
    <rect class="card-bg-blue" x="671" y="75" width="523" height="298"/>
    <polygon class="bubble-white" points="762,95 1115,75 1194,240 1170,355 1060,345 960,373 880,373 890,325 742,315"/>
    <polygon class="bubble-blue" points="790,120 1110,90 1165,250 1140,285 1120,315 1010,305 930,373 935,300 775,285"/>
    <polyline class="stripe" points="1150,100 1188,215"/>
    <polyline class="stripe" points="748,145 744,260"/>
    <polyline class="stripe" points="1180,285 1145,285 1160,350 1070,342"/>
    <polyline class="stripe" points="1015,350 985,373"/>
    <polyline class="dash-blue" points="745,315 890,328"/>
    <circle class="brand-dot" cx="846" cy="188" r="12"/>
    <text class="brand-name" x="882" y="207" font-size="30">ROAM QUILL</text>
    <text class="brand-url" x="875" y="256" font-size="17">www.roamquill.net</text>
  </g>

  <!-- Row 2 front -->
  <g class="card card-front" clip-path="url(#c3)">
    <rect class="card-bg-blue" x="91" y="461" width="523" height="297"/>
    <polyline class="dash-light" points="138,461 118,685 270,697 252,758"/>
    <polyline class="dash-light" points="537,461 598,655 573,655"/>
    <polyline class="stripe" points="133,510 120,630"/>
    <polyline class="stripe" points="540,470 578,600"/>
    <polyline class="stripe" points="572,655 532,655 550,722 430,712"/>
    <polyline class="stripe" points="400,720 350,758"/>
    <polygon class="bubble-white" points="165,485 505,462 507,685 160,655"/>
    <polygon fill="url(#tailShade)" points="320,668 410,680 285,758"/>
    <polygon class="tag-sky" points="376,505 515,470 555,622 380,622"/>
    <rect class="art-slot" x="388" y="505" width="122" height="105" role="img" aria-label="Illustration of a white camel"/>
    <text class="holder-name" x="176" y="534" font-size="19">BERTRAND OLESKY</text>
    <text class="contact" x="177" y="565" font-size="16.5">+1-(345)-402-7731</text>
    <text class="contact" x="177" y="587" font-size="16.5">ceo@roamquill.net</text>
    <text class="address" x="165" y="647" font-size="14" transform="rotate(4.5 165 647)">Coral Reach Shore, Grand Cayman, Cayman Islands</text>
  </g>

  <!-- Row 2 back -->
  <g class="card card-back" clip-path="url(#c4)">
    <rect class="card-bg-white" x="677" y="461" width="523" height="297"/>
    <polyline class="dash-blue" points="840,463 747,480 728,700 875,715 858,758"/>
    <polyline class="dash-blue" points="1125,461 1195,672 1170,672"/>
    <polyline class="stripe" points="745,520 732,650"/>
    <polyline class="stripe" points="840,464 880,461"/>
    <polyline class="stripe" points="1138,490 1180,630"/>
    <polyline class="stripe" points="1168,672 1130,672 1148,738 1040,728"/>
    <polyline class="stripe" points="1000,735 970,758"/>
    <polygon class="bubble-blue" points="775,505 1080,461 1145,640 1085,645 1105,700 1010,695 895,758 905,695 760,672"/>
    <circle class="brand-dot" cx="830" cy="575" r="12"/>
    <text class="brand-name" x="868" y="595" font-size="29">ROAM QUILL</text>
    <text class="brand-url" x="860" y="644" font-size="17">www.roamquill.net</text>
  </g>

  <!-- Row 3 front -->
  <g class="card card-front" clip-path="url(#c5)">
    <rect class="card-bg-blue" x="91" y="841" width="523" height="297"/>
    <polyline class="dash-light" points="165,841 108,1032 140,1035"/>
    <polyline class="dash-light" points="567,841 587,1065 430,1078 450,1138"/>
    <polyline class="stripe" points="165,850 128,965"/>
    <polyline class="stripe" points="572,890 584,1010"/>
    <polyline class="stripe" points="132,1032 175,1032 155,1100 280,1092"/>
    <polyline class="stripe" points="300,1100 360,1138"/>
    <polygon class="bubble-white" points="255,841 540,863 553,1035 205,1060 215,1000"/>
    <polygon fill="url(#tailShade)" points="295,1055 392,1045 420,1138"/>
    <polygon class="tag-sky" points="200,843 335,885 328,1000 150,1003"/>
    <rect class="art-slot" x="195" y="885" width="125" height="105" role="img" aria-label="Illustration of a white camel"/>
    <text class="holder-name" x="343" y="915" font-size="19">BERTRAND OLESKY</text>
    <text class="contact" x="343" y="945" font-size="16.5">+1-(345)-402-7731</text>
    <text class="contact" x="343" y="968" font-size="16.5">ceo@roamquill.net</text>
    <text class="address" x="210" y="1052" font-size="14" transform="rotate(-4 210 1052)">Coral Reach Shore, Grand Cayman, Cayman Islands</text>
  </g>

  <!-- Row 3 back -->
  <g class="card card-back" clip-path="url(#c6)">
    <rect class="card-bg-white" x="677" y="841" width="523" height="297"/>
    <polyline class="dash-blue" points="752,841 692,1032 722,1035"/>
    <polyline class="dash-blue" points="1155,845 1172,1062 1020,1078 1040,1138"/>
    <polyline class="stripe" points="750,852 714,965"/>
    <polyline class="stripe" points="1158,890 1170,1010"/>
    <polyline class="stripe" points="720,1032 760,1032 742,1100 860,1092"/>
    <polyline class="stripe" points="890,1100 945,1138"/>
    <polyline class="stripe" points="1032,1110 1045,1138"/>
    <polygon class="bubble-blue" points="780,841 1125,862 1140,1035 975,1050 1005,1138 885,1055 740,1000"/>
    <circle class="brand-dot" cx="818" cy="930" r="12"/>
    <text class="brand-name" x="855" y="950" font-size="29">ROAM QUILL</text>
    <text class="brand-url" x="850" y="1000" font-size="17">www.roamquill.net</text>
  </g>
</svg>
</body>
</html>
```